Pull-up Banner Design Project

We are a managed account investment company specialising in financial derivatives. Sydney based, our team combines over 100 years of financial markets experience. Our advisers trade the worlds financial markets directly on the clients account whilst the client retains full access and control of the account.
We are holding a seminar in September (and potentially more next year) to showcase our specialist investment program and need to create TWO pull-up banners for the event. The banners need to compliment each other as a Right side, Left side of the stage or presenter, however they should be able to be deployed independently. The size of the banners will be approx 120 cm wide by 200 cm tall.
We have an approved company colour pallet, logos and images. I have provided JPEG versions of these however they can be supplied in Bitmap or GIF if required.
Target Market(s)
Self Managed Superannuation Fund Trustees (Individual Investors)
Industry/Entity Type
Investment
Requirements
Must have
- - Two banner designs - One Right of Stage and one Left of Stage
- Company approved logo
- Company approved colour pallet
- Company approved images
- Can be used independently
- Website: www.korvenpartners.com.au (can be smallish print)
- Phone: 1300 416 748 (can be smallish print)
Should not have
- Absolutely no images of obscene wealth such as palm trees or speed boats or similar... approved images only.

```html
<!DOCTYPE html>
<html lang="en">
<head>
<meta charset="utf-8">
<title>Korven Partners – Pull-up Banners</title>
<link rel="stylesheet" href="https://fonts.googleapis.com/css2?family=Open+Sans:wght@600;700&display=swap">
<style>
  :root {
    --page-bg: #e4e4e4;
    --banner-bg: #ffffff;
    --brand-green: #2f5e45;
    --accent-tan: #b8ab8c;
    --ink: #1c1c1c;
    --footer-ink: #ffffff;
    --stone-light: #d4d4d4;
    --stone-mid: #9a9a9a;
    --stone-dark: #4a4a4a;
    --sky-light: #c9d8ee;
    --sky-mid: #5a7fc0;
    --glass-dark: #233047;
  }
  * { margin: 0; padding: 0; box-sizing: border-box; }
  html, body { width: 1200px; height: 900px; overflow: hidden; }
  body {
    background: var(--page-bg);
    font-family: "Open Sans", Arial, sans-serif;
    position: relative;
  }
  .banner {
    position: absolute;
    top: 56px;
    width: 480px;
    height: 799px;
    background: var(--banner-bg);
    box-shadow: 0 2px 8px rgba(0,0,0,0.25);
    overflow: hidden;
  }
  .banner--left { left: 61px; }
  .banner--right { left: 639px; }

  .brand-name {
    position: absolute;
    top: 62px;
    left: 0;
    width: 100%;
    text-align: center;
    color: var(--brand-green);
    font-weight: 700;
    font-size: 42px;
    letter-spacing: 1px;
    line-height: 56px;
    text-transform: uppercase;
  }

  .tagline {
    position: absolute;
    left: 0;
    width: 100%;
    text-align: center;
    color: var(--ink);
    font-weight: 600;
    font-size: 26px;
    line-height: 39px;
  }
  .banner--left .tagline { top: 173px; }
  .banner--right .tagline { top: 186px; line-height: 42px; }

  .photo {
    position: absolute;
    left: 0;
    width: 100%;
    top: 344px;
    height: 353px;
  }
  .photo--stones {
    background: linear-gradient(to bottom, #ffffff 0%, var(--stone-light) 22%, var(--stone-mid) 60%, var(--stone-dark) 100%);
  }
  .photo--towers {
    top: 360px;
    height: 337px;
    background:
      linear-gradient(to bottom, #ffffff 0%, rgba(255,255,255,0) 18%),
      linear-gradient(100deg, var(--glass-dark) 0%, #47618d 22%, var(--sky-mid) 35%, var(--sky-light) 70%, #eef3fa 100%);
  }

  .trim {
    position: absolute;
    left: 0;
    top: 697px;
    width: 100%;
    height: 6px;
    background: var(--accent-tan);
  }
  .contact {
    position: absolute;
    left: 0;
    top: 703px;
    width: 100%;
    height: 96px;
    background: var(--brand-green);
    color: var(--footer-ink);
    text-align: center;
    font-weight: 700;
    font-size: 24px;
    line-height: 32px;
    padding-top: 16px;
  }
</style>
</head>
<body>
  <section class="banner banner--left">
    <div class="brand-name">Korven Partners</div>
    <p class="tagline">Contemporary<br>Collaborative<br>Professional<br>Leading</p>
    <div class="photo photo--stones" role="img" aria-label="Black and white photo of smooth stepping stones curving across still water"></div>
    <div class="trim"></div>
    <div class="contact">
      <div class="contact-web">www.korvenpartners.com.au</div>
      <div class="contact-phone">Phone: 1300 416 748</div>
    </div>
  </section>

  <section class="banner banner--right">
    <div class="brand-name">Korven Partners</div>
    <p class="tagline">Absolute returns through<br>the worlds capital markets</p>
    <div class="photo photo--towers" role="img" aria-label="Upward view of glass office towers against a blue sky with white clouds"></div>
    <div class="trim"></div>
    <div class="contact">
      <div class="contact-web">www.korvenpartners.com.au</div>
      <div class="contact-phone">Phone: 1300 416 748</div>
    </div>
  </section>
</body>
</html>
```